Automotive Accessories Business Card

Design a business template that match our new logo design and our industry.

https://www.kelvramotive.com/

Target Market(s)

Aftermarket auto parts and accessories

Industry/Entity Type

automotive

Contact Information for Business Card

company logo

Font styles to use
Serif
Sans Serif

Colors
EB3D1F
EC4F4E
F09395
F8D3D4
FCEDEE

```html
<!DOCTYPE html>
<html lang="en">
<head>
<meta charset="utf-8">
<title>Kelvra Motive Business Card</title>
<link rel="stylesheet" href="https://fonts.googleapis.com/css2?family=Montserrat:wght@400;500;700;800&display=swap">
<style>
  :root {
    --bg: #e9e9ea;
    --card-white: #ffffff;
    --brand-red: #d41f26;
    --brand-red-deep: #b3151c;
    --ink: #3b3b3d;
    --ink-soft: #555558;
    --rule: #8a8a8c;
  }
  * { margin: 0; padding: 0; box-sizing: border-box; }
  html, body { width: 1200px; height: 802px; overflow: hidden; }
  body {
    background: var(--bg);
    font-family: "Montserrat", sans-serif;
    display: flex;
    align-items: center;
    justify-content: center;
    gap: 48px;
  }
  .card {
    width: 525px;
    height: 300px;
    border-radius: 2px;
    box-shadow: 0 10px 30px rgba(0,0,0,0.12);
    position: relative;
    overflow: hidden;
  }
  .card--front {
    background: var(--card-white);
    border-bottom: 4px solid var(--brand-red);
    display: flex;
    align-items: center;
  }
  .brand-block {
    width: 245px;
    display: flex;
    align-items: center;
    justify-content: center;
    gap: 10px;
  }
  .brand-mark {
    width: 16px; height: 16px;
    background: var(--brand-red);
  }
  .brand-name {
    font-weight: 800;
    font-size: 22px;
    line-height: 1.05;
    color: var(--ink);
    letter-spacing: 0.5px;
  }
  .divider {
    width: 1px;
    height: 130px;
    background: var(--rule);
  }
  .contact-block {
    padding-left: 26px;
    color: var(--ink-soft);
    font-size: 12.5px;
    line-height: 1.45;
  }
  .person-name {
    font-weight: 800;
    font-size: 19px;
    color: var(--brand-red);
    letter-spacing: 1px;
    line-height: 1.1;
  }
  .person-title { margin-bottom: 12px; }
  .address { margin-bottom: 12px; }
  .contact-line { display: flex; align-items: center; gap: 7px; }
  .contact-line svg { width: 11px; height: 11px; fill: var(--brand-red); flex: none; }
  .card--back {
    background: var(--brand-red);
    display: flex;
    align-items: center;
    justify-content: center;
    gap: 16px;
  }
  .back-mark {
    width: 28px; height: 28px;
    background: var(--brand-red-deep);
  }
  .back-name {
    font-weight: 800;
    font-size: 44px;
    line-height: 1;
    color: var(--brand-red-deep);
    letter-spacing: 1px;
  }
</style>
</head>
<body>
  <section class="card card--front">
    <div class="brand-block">
      <span class="brand-mark"></span>
      <span class="brand-name">KELVRA<br>MOTIVE INC</span>
    </div>
    <div class="divider"></div>
    <div class="contact-block">
      <p class="person-name">DANIEL REYES</p>
      <p class="person-title">Manager</p>
      <p class="address">48 Harlow Ave. Unit B<br>Fairmont, CA 90317</p>
      <p class="contact-line">
        <svg viewBox="0 0 24 24" aria-hidden="true"><path d="M6.6 10.8a15.1 15.1 0 0 0 6.6 6.6l2.2-2.2a1 1 0 0 1 1-.25 11.4 11.4 0 0 0 3.6.57 1 1 0 0 1 1 1V20a1 1 0 0 1-1 1A17 17 0 0 1 3 4a1 1 0 0 1 1-1h3.5a1 1 0 0 1 1 1c0 1.25.2 2.45.57 3.57a1 1 0 0 1-.25 1z"/></svg>
        1-800-555-0142
      </p>
      <p class="contact-line">
        <svg viewBox="0 0 24 24" aria-hidden="true"><path d="M2 5h20v14H2z M2 5l10 8 10-8" fill="none" stroke="#d41f26" stroke-width="2.4"/></svg>
        sales@kelvramotive.com
      </p>
      <p class="contact-line">
        <svg viewBox="0 0 24 24" aria-hidden="true"><circle cx="12" cy="12" r="10"/><path d="M2 12h20M12 2c3 3 3 17 0 20M12 2c-3 3-3 17 0 20" fill="none" stroke="#fff" stroke-width="1.6"/></svg>
        www.kelvramotive.com
      </p>
    </div>
  </section>

  <section class="card card--back">
    <span class="back-mark"></span>
    <span class="back-name">KELVRA MOTIVE</span>
  </section>
</body>
</html>
```